2nd Opinion Radiology web page

Looking for a web page design for second opinion radiology service. Main page will have a link directing user to locate CD on their computer/device, and will take contents of CD and upload to server, which I will specify.

Web page needs a form to enter user's name, contact info, and create a log in for user. User must click to accept terms of service, which will be a paragraph which i will provide. User will log back in, after uploading cd, to find report, which will be able to be viewed once user pays, by coinvera. User will need to be able to download report.

There will be a small paragraph explaining what we do: Provide expert second opinions, worldwide. We provide interpretations from radiologists with many years of experience and training from the world's best institutions, including brennick and corvalen regional hospital.

A second paragraph: Have questions or doubts about your CT or MRI? Get a second opinion from experts at ScanPerch. Tap into the full potential of your images.

Thanks

Reason: The website does not need to be fully coded, however, should include graphics and design so a web designer can simply take the design, images, and objects and code the site.

People who are unsure of their medical care and looking for a second opinion.

Training

```html
<!DOCTYPE html>
<html lang="en">
<head>
<meta charset="utf-8">
<title>ScanPerch — Expert 2nd Opinions</title>
<link rel="stylesheet" href="https://fonts.googleapis.com/css2?family=PT+Sans:wght@400;700&family=Baumans&family=Arimo:wght@400;700&display=swap">
<style>
  :root {
    --teal-dark: #215a78;
    --teal-line: #3d7e9a;
    --ink-grey: #6b6b6b;
    --tagline-grey: #7d7d7d;
    --accent-green: #a5ab1a;
    --button-top: #bccb2c;
    --button-bottom: #8e9f12;
    --field-bg: #efefef;
    --field-border: #dcdcdc;
    --field-text: #707070;
    --footer-rule: #b9b9b9;
    --footer-copy: #8a8a8a;
    --white: #ffffff;
  }
  * { box-sizing: border-box; margin: 0; padding: 0; }
  html, body { width: 1200px; height: 1096px; overflow: hidden; background: var(--white); }
  body { position: relative; font-family: "Arimo", Arial, sans-serif; }

  .brand {
    position: absolute; left: 23px; top: 28px;
    display: flex; align-items: center; gap: 12px;
    font-family: "PT Sans", sans-serif; font-weight: 700;
    font-size: 46px; letter-spacing: 1px; color: var(--teal-dark);
  }
  .brand-mark { width: 30px; height: 30px; background: var(--teal-dark); border-radius: 4px; }

  .tagline {
    position: absolute; left: 381px; top: 44px;
    font-family: "PT Sans", sans-serif; font-size: 29px; letter-spacing: 0.5px;
    color: var(--tagline-grey);
  }
  .tagline strong { font-weight: 700; color: #6e6e6e; }

  .main-nav { position: absolute; top: 122px; left: 0; width: 1200px; height: 36px; }
  .main-nav a {
    position: absolute; top: 0;
    font-family: "Baumans", sans-serif; font-size: 22px; color: var(--teal-dark);
    text-decoration: none; letter-spacing: 0.5px;
  }
  .main-nav a.is-current::after {
    content: ""; position: absolute; left: 50%; top: 29px; margin-left: -7px;
    border-left: 7px solid transparent; border-right: 7px solid transparent;
    border-bottom: 8px solid var(--accent-green);
  }

  .account-tabs a {
    position: absolute; top: 115px; height: 44px;
    background: var(--teal-dark); color: var(--white);
    border-radius: 10px 10px 0 0;
    font-family: "Baumans", sans-serif; font-size: 17px;
    display: flex; align-items: center; justify-content: center;
    text-decoration: none;
  }
  .tab-signin { left: 991px; width: 91px; }
  .tab-signup { left: 1086px; width: 92px; }

  .nav-rule { position: absolute; left: 0; top: 158px; width: 1200px; height: 3px; background: var(--teal-line); }

  .hero {
    position: absolute; left: 0; top: 161px; width: 1200px; height: 541px;
    background: linear-gradient(90deg, #2a2a2c 0%, #5c5f63 25%, #d9d2c4 50%, #c9ad98 70%, #e8e6e4 100%);
  }

  .signup-card {
    position: absolute; left: 171px; top: 233px; width: 379px; height: 355px;
    background: var(--white); border-radius: 24px;
  }
  .signup-card h2 {
    position: absolute; left: 26px; top: 22px;
    font-family: "PT Sans", sans-serif; font-weight: 700; font-size: 29px; color: var(--teal-dark);
  }
  .field {
    position: absolute; left: 35px; width: 305px; height: 39px;
    background: var(--field-bg); border: 1px solid var(--field-border); border-radius: 20px;
    padding-left: 24px; display: flex; align-items: center;
    font-size: 15px; font-weight: 700; color: var(--field-text);
  }
  .field-name { top: 68px; }
  .field-email { top: 120px; }
  .field-phone { top: 171px; }
  .terms {
    position: absolute; left: 45px; top: 230px;
    display: flex; align-items: center; gap: 7px;
    font-size: 13px; color: #555;
  }
  .terms-radio { width: 14px; height: 14px; border-radius: 50%; border: 1px solid #999; background: linear-gradient(#f4f4f4, #cfcfcf); }
  .terms a { color: var(--teal-dark); text-decoration: underline; }
  .signup-button {
    position: absolute; left: 41px; top: 270px; width: 117px; height: 37px;
    background: linear-gradient(var(--button-top), var(--button-bottom));
    border-radius: 3px; color: var(--white);
    font-size: 15px; font-weight: 700; letter-spacing: 0.5px;
    display: flex; align-items: center; justify-content: center;
  }

  .about { position: absolute; left: 39px; top: 736px; width: 1120px; }
  .about h1 {
    font-family: "PT Sans", sans-serif; font-weight: 400; font-size: 37px;
    color: var(--teal-dark); letter-spacing: 0.5px;
  }
  .about p { font-size: 19.5px; line-height: 24px; color: var(--ink-grey); }
  .about .intro { margin-top: 19px; }
  .about .pitch { margin-top: 33px; }
  .pitch-question { color: var(--accent-green); }
  .pitch-offer { color: var(--teal-dark); }

  .footer-rule { position: absolute; left: 0; top: 1007px; width: 1200px; height: 1px; background: var(--footer-rule); }
  .footer-links { position: absolute; left: 36px; top: 1028px; font-size: 14.5px; color: var(--teal-dark); }
  .footer-links a { color: var(--teal-dark); text-decoration: none; }
  .footer-copy { position: absolute; left: 34px; top: 1055px; font-size: 13px; color: var(--footer-copy); }
</style>
</head>
<body>
  <header>
    <div class="brand"><span class="brand-mark"></span>SCANPERCH</div>
    <p class="tagline">PROVIDING EXPERT <strong>2ND OPINIONS</strong> WORLD WIDE</p>
    <nav class="main-nav">
      <a class="is-current" href="#" style="left:27px">HOME</a>
      <a href="#" style="left:147px">WHY US</a>
      <a href="#" style="left:288px">WHO WE ARE</a>
      <a href="#" style="left:476px">CONTACT US</a>
    </nav>
    <div class="account-tabs">
      <a class="tab-signin" href="#">SIGN IN</a>
      <a class="tab-signup" href="#">SIGN UP</a>
    </div>
    <div class="nav-rule"></div>
  </header>

  <section class="hero" role="img" aria-label="Photo of a thoughtful doctor beside monitors showing brain MRI scans"></section>

  <form class="signup-card">
    <h2>Create Account</h2>
    <div class="field field-name">name</div>
    <div class="field field-email">email address</div>
    <div class="field field-phone">contact number</div>
    <label class="terms"><span class="terms-radio"></span>I agree to the <a href="#">Terms of Service</a></label>
    <div class="signup-button">SIGN UP</div>
  </form>

  <main class="about">
    <h1>WHAT WE DO</h1>
    <p class="intro">Provide expert second opinions, worldwide. We provide interpretations from radiologists with many years of experience and training from the world's best institutions, including brennick and corvalen regional hospital.</p>
    <p class="pitch"><span class="pitch-question">Have questions or doubts about your CT or MRI?</span> <span class="pitch-offer">Get a second opinion from experts at ScanPerch</span>. Tap into the full potential of your images.</p>
  </main>

  <footer>
    <div class="footer-rule"></div>
    <p class="footer-links"><a href="#">Home</a> · <a href="#">Why us</a> · <a href="#">Who we are</a> · <a href="#">Contact Us</a> · <a href="#">Terms of Use</a></p>
    <p class="footer-copy">© Copyright 2013 Scan Perch. All rights reserved.</p>
  </footer>
</body>
</html>
```